Folded Business Cards, Envelopes, Information card and Thank You card.
Gala Tent Company
Folded Business Cards, Envelopes, Information card and Thank You card. - Events
Creative Brief
Modern
Marisol Fenwick-Dutra
Owner-Linen Specialist
2718 Harbor Crest Ave Suite 204B Long Beach CA 90807
marisol@larkspurdrapery.example
larkspurdraperys.example
Our colors are silver, grey, dark plum and eggplant. I would like something modern with maybe translucent floral scrolls in the background. I am open to card back ground color. It can be silver, plum/eggplant or even white. We are a high-end wedding linen rental company. Our clients are mostly female, mid income and are planning a wedding. I am looking for the following items: 1. Business Card. 2. Envelope. 3. Information Card. 4. Thank You Card. Information Card: This is an information card that will be sent out with each order. It will be printed on a 6" x 9" post card one sided. Bellow is the text that will go on the card Important Information Regarding Your Linen Returns. Thank you for allowing Larkspur Drapery linens to share in your special day. To ensure prompt return of your linens, please follow the steps bellow. 1. Please place all linens in the included return duffel bags or the box they arrived in. It returning in a box, please fold linens so that they all fit in the box. Please shake any loose food from linens and insure linens are dry prior to placing in box and bags. NEVER place wet linens in bags, boxes of plastic. If your linens are wet or damp please allow them to air dry prior to packing. If your shipment included chair sashes, please remember to untie each sash prior to return. You account will be billed a fee of $.25 for each sash returned that is untied. 2. If you would like to schedule a ParcelWing pickup, please contact ParcelWing the day PRIOR to your scheduled return date as ParcelWing does not do same pickup. Please note, ParcelWing charges a pickup fee of $8. This fee is paid directly to ParcelWing. You can contact ParcelWing at 1.800.Go.Wing (555-0148). You may also return your linens for free of charge by dropping of your linens at any ParcelWing or ParcelWing Copyhub. Please use the attached pre-paid ParcelWing air-bil that came with your shipment. Lost ParcelWing Air-Bills: Please treat your ParcelWing return air-bills as cash. If they are lost or damaged, please contact us as soon as possible for replacements. We charge a fee of $25 for each lost or damaged air-bill that needs to be replaced. Alternate Shipping Carriers: Your linen rental includes pre-paid return shipping via ParcelWing and include tracking for our warehouse. Please do not return linens using any other shipping provider or any other class of shipping (i.e. Express, Next Day, Over Night these services will be billed back to your account). Late Returns: Our customers depend on your timely return. Please insure our items are dropped off or picked up by ParcelWing the following business day after your event. Items shipped back after the due date are considered late and will be charge a rental fee equal to 50% of your original rental rate prior to any discounts or promotions. Should you have any questions regarding your order please contact our office at 562.555.0173 should you need to reach us after hours or on weekends please leave a message or send an e-mail to afterhours@larkspurdraperys.example. Thank you card: Please also design a matching thank you card that will be printed on a 4" x 6" one sided post card.
Notes: We are using a folded business card: We would like it laid out as follows: Front: Logo with contact details Inside: The inside will have a space where we can glue on a fabric swatch. We would like the swatch to be placed placed in a decorative rectangle that should take up most of the inside. There also needs to be wording under the square that says "Raspberry Satin Back Shantung" we would like this centered. Back: On the back of the card we would like: twitter icon with our twitter id:larkspurcloth youtube logo with our id: larkspurdraperys

```html
<!DOCTYPE html>
<html lang="en">
<head>
<meta charset="utf-8">
<title>Larkspur Drapery linens – Stationery Set</title>
<link href="https://fonts.googleapis.com/css2?family=Cinzel:wght@400;600&family=Open+Sans:wght@400;600;700&display=swap" rel="stylesheet">
<style>
:root{
  --plum:#4b2a72;
  --eggplant:#3a1f5a;
  --grey:#8c8c8c;
  --silver:#c9c9cb;
  --ink:#4a4a4a;
  --paper:#ffffff;
  --stage:#e7e5e2;
}
*{margin:0;padding:0;box-sizing:border-box}
html,body{width:1200px;height:866px;overflow:hidden;background:var(--stage)}
.canvas{position:relative;width:1200px;height:866px}
.piece{position:absolute;background:var(--paper);box-shadow:0 2px 6px rgba(0,0,0,.18);overflow:hidden}
.serif{font-family:'Cinzel',serif}
.sans{font-family:'Open Sans',sans-serif}
.brand{display:flex;align-items:center;gap:6px;color:var(--grey);font-family:'Cinzel',serif;font-weight:600;letter-spacing:.08em;text-transform:uppercase;white-space:nowrap}
.brand .mark{display:inline-block;background:var(--grey)}

/* Thank-you note card */
.note-card{left:204px;top:100px;width:180px;height:392px}
.note-card .message{position:absolute;left:20px;right:14px;bottom:56px;font-family:'Cinzel',serif;font-size:8.4px;line-height:1.55;letter-spacing:.06em;color:var(--ink);text-transform:uppercase}

/* Folded thank-you card */
.fold-card{left:408px;top:96px;width:192px;height:420px}
.fold-card .band{position:absolute;left:0;top:0;width:100%;height:205px;background:var(--plum);border-bottom:1px solid #ddd}
.fold-card .band .brand{position:absolute;left:50%;top:70px;transform:translateX(-50%) rotate(180deg);flex-direction:column;color:#fff;font-size:10px;gap:8px}
.fold-card .band .brand .mark{width:26px;height:26px;background:#fff}
.fold-card .lower{position:absolute;left:0;top:205px;width:100%;height:215px;display:flex;flex-direction:column;align-items:center;justify-content:center;gap:30px}
.fold-card .lower .mark{width:32px;height:32px;background:var(--grey)}
.fold-card .thanks{font-family:'Cinzel',serif;font-size:13px;color:var(--plum);letter-spacing:.06em;margin-top:34px}

/* Envelopes */
.envelope{left:636px;width:408px;height:200px}
.envelope.back{top:108px}
.envelope.front{top:318px}
.envelope svg{position:absolute;left:0;top:0}
.envelope .seal{position:absolute;left:50%;transform:translateX(-50%);width:28px;height:28px;background:var(--paper)}
.envelope.back .seal{top:48px;background:var(--grey)}
.envelope.front .seal{top:48px;background:var(--grey)}

/* Information card */
.info-card{left:91px;top:533px;width:533px;height:271px;padding:12px 16px}
.info-card header{display:flex;align-items:flex-start;gap:30px;margin-bottom:8px}
.info-card header .brand{font-size:10px}
.info-card header .brand .mark{width:26px;height:26px}
.info-card h1{font-family:'Open Sans',sans-serif;font-weight:700;font-size:13px;line-height:1.2;color:var(--plum);text-align:center;flex:1}
.info-card p,.info-card .col{font-family:'Open Sans',sans-serif;font-size:4.9px;line-height:1.45;color:var(--ink)}
.info-card p{margin-bottom:4px}
.info-card .cols{display:grid;grid-template-columns:1fr 1fr 1fr;gap:12px;margin-top:4px}
.info-card .col strong{display:block;font-weight:700;margin-bottom:1px}
.info-card .footer{position:absolute;left:16px;right:16px;bottom:10px;text-align:center}

/* Folded business card */
.biz-card{left:643px;top:576px;width:245px;height:216px}
.biz-card .back{position:absolute;left:0;top:0;width:100%;height:72px;background:#f4f4f5;border-bottom:1px solid #ddd;padding:10px 14px;display:flex;flex-direction:column;gap:8px}
.biz-card .social{display:flex;align-items:center;gap:5px;font-family:'Open Sans',sans-serif;font-size:6.5px;color:var(--ink)}
.biz-card .social .dot{width:9px;height:9px;border-radius:50%;background:var(--plum)}
.biz-card .social .sq{width:9px;height:9px;background:var(--grey)}
.biz-card .front{position:absolute;left:0;top:72px;width:100%;height:144px}
.biz-card .rule{position:absolute;left:0;right:0;top:0;height:4px;background:var(--plum)}
.biz-card .contact{position:absolute;left:14px;top:20px;font-family:'Open Sans',sans-serif;font-size:5.6px;line-height:1.6;color:var(--ink);width:100px}
.biz-card .contact .name{font-weight:700;font-size:6.6px;color:var(--plum)}
.biz-card .front .brand{position:absolute;right:12px;bottom:26px;flex-direction:column;gap:6px;font-size:9px}
.biz-card .front .brand .mark{width:22px;height:22px}

/* Swatch card */
.swatch-card{left:900px;top:576px;width:216px;height:216px}
.swatch-card .frame{position:absolute;left:18px;top:16px;right:18px;bottom:42px;border:1px solid #e6e6e8}
.swatch-card .label{position:absolute;left:0;right:0;bottom:16px;text-align:center;font-family:'Cinzel',serif;font-size:10px;color:var(--plum);letter-spacing:.02em}
</style>
</head>
<body>
<main class="canvas">

  <section class="piece note-card" aria-label="Thank you note card">
    <p class="message">Thank you for allowing Larkspur Drapery linens to share in your special day. It was a pleasure working with you and we look forward to working with you in the near future.</p>
  </section>

  <section class="piece fold-card" aria-label="Folded thank you card">
    <div class="band">
      <div class="brand"><span class="mark"></span><span>Larkspur Drapery</span></div>
    </div>
    <div class="lower">
      <span class="mark"></span>
      <span class="thanks">Thank You !</span>
    </div>
  </section>

  <section class="piece envelope back" aria-label="Envelope, back">
    <svg width="408" height="200" viewBox="0 0 408 200">
      <polygon points="0,0 408,0 408,18 204,110 0,18" fill="var(--plum)"/>
      <polyline points="0,200 170,100" stroke="#e2e2e2" fill="none"/>
      <polyline points="408,200 238,100" stroke="#e2e2e2" fill="none"/>
    </svg>
    <span class="seal"></span>
  </section>

  <section class="piece envelope front" aria-label="Envelope, flap open">
    <svg width="408" height="200" viewBox="0 0 408 200">
      <polygon points="0,0 408,0 408,14 204,105 0,14" fill="var(--silver)"/>
      <polygon points="0,0 408,0 408,6 204,96 0,6" fill="var(--grey)"/>
    </svg>
    <span class="seal"></span>
  </section>

  <section class="piece info-card" aria-label="Linen returns information card">
    <header>
      <div class="brand"><span class="mark"></span><span>Larkspur Drapery</span></div>
      <h1>Important Information Regarding<br>Your Linen Returns.</h1>
    </header>
    <p>Thank you for allowing Larkspur Drapery linens to share in your special day. To ensure prompt return of your linens, please follow the steps bellow.</p>
    <p>1. Please place all linens in the included return duffel bags or the box they arrived in. It returning in a box, please fold linens so that they all fit in the box. Please shake any loose food from linens and insure linens are dry prior to placing in box and bags. NEVER place wet linens in bags, boxes of plastic. If your linens are wet or damp please allow them to air dry prior to packing. If your shipment included chair sashes, please remember to untie each sash prior to return. You account will be billed a fee of $.25 for each sash returned that is untied.</p>
    <p>2. If you would like to schedule a ParcelWing pickup, please contact ParcelWing the day PRIOR to your scheduled return date as ParcelWing does not do same pickup. Please note, ParcelWing charges a pickup fee of $8. This fee is paid directly to ParcelWing. You can contact ParcelWing at 1.800.Go.Wing (555-0148). You may also return your linens for free of charge by dropping of your linens at any ParcelWing or ParcelWing Copyhub. Please use the attached pre-paid ParcelWing air-bil that came with your shipment.</p>
    <div class="cols">
      <div class="col"><strong>Lost ParcelWing Air-Bills:</strong>Please treat your ParcelWing return air-bills as cash. If they are lost or damaged, please contact us as soon as possible for replacements. We charge a fee of $25 for each lost or damaged air-bill that needs to be replaced.</div>
      <div class="col"><strong>Alternate Shipping Carriers:</strong>Your linen rental includes pre-paid return shipping via ParcelWing and include tracking for our warehouse. Please do not return linens using any other shipping provider or any other class of shipping (i.e. Express, Next Day, Over Night these services will be billed back to your account).</div>
      <div class="col"><strong>Late Returns:</strong>Our customers depend on your timely return. Please insure our items are dropped off or picked up by ParcelWing the following business day after your event. Items shipped back after the due date are considered late and will be charge a rental fee equal to 50% of your original rental rate prior to any discounts or promotions.</div>
    </div>
    <p class="footer">Should you have any questions regarding your order please contact our office at 562.555.0173 should you need to reach us after hours or on weekends please leave a message or send an e-mail to afterhours@larkspurdraperys.example.</p>
  </section>

  <section class="piece biz-card" aria-label="Folded business card">
    <div class="back">
      <div class="social"><span class="dot"></span><span>larkspurcloth</span></div>
      <div class="social"><span class="sq"></span><span>larkspurdraperys</span></div>
    </div>
    <div class="front">
      <span class="rule"></span>
      <div class="contact">
        <div class="name">Marisol Fenwick-Dutra</div>
        <div>Owner-Linen Specialist</div>
        <div>2718 Harbor Crest Ave Suite 204B<br>Long Beach CA 90807</div>
        <div>marisol@larkspurdrapery.example</div>
        <div>larkspurdraperys.example</div>
      </div>
      <div class="brand"><span class="mark"></span><span>Larkspur Drapery</span></div>
    </div>
  </section>

  <section class="piece swatch-card" aria-label="Fabric swatch card">
    <div class="frame"></div>
    <p class="label">Raspberry Satin Back Shantung</p>
  </section>

</main>
</body>
</html>
```